For Creative Minds: A Simple Clean Book Cover that Stands Out

This will be a christian book teaching christians about divine healing. It is part of a series called "Forty Morning Set". I want the book cover to communicate the idea of healing, and specifically heavenly healing from God. These are some of the specifications below

1. General
Book to be published on print lantern platform
Dimensions: 6 x 9 inches, Paperback
Number of words: Estimated to be about 60,000 words.
Please use Indesign for design and submit the final Indesign source files along with the final design.

2. Cover image.
Image can be either human or any object that can communicate the idea above. No human faces to show up prominently.
High quality image is highly solicited.

3. Title:
" Forty Mornings to Claim and Hold Your Heavenly Restoration"

3. Author name
Preferably should appear below. Open to creative ideas with titles that are better placed above.

Author's Name: Daniel Fesch

3. Layout
Should not be too busy.
Simple and clean layout appeals more to me.

4. Series name
AS noted above, this book will be part of a series called " Forty Morning Set". I want this series name to appear somewhere in the cover and to have a simple but unique design that will be used for all subsequent titles. The Title of the book should have the emphasis.

I have attached a sample cover for one of my monthly devotional books which I choose from a contest.

ABOUT THE AUTHOR
Daniel Fesch represents the blessed combination of Physician and Minister, bringing healing not only to the physical body but to the spiritual heart. He currently works as the Director of the Hospital Medicine Program at the Brellmont County Care Campus in Iowa, USA. He is the Founder of Lantern & Vine Fellowship, a teaching ministry that seeks to bring believers into the fullness of grace — the glory of God — through conferences, seminars and books.

One of his notable quotes is “The Word of God is the most potent and efficient remedy for all the ailments of humanity.” This clearly portrays his experience with the Word as a Physician who is familiar with the powers, both natural and supernatural, to mend broken human beings. 

He currently lives in Iowa, USA with his wife, Tessa Lund, and daughter, Rosalind. You can reach out to Daniel using the contact information listed below.

BLURB
As a Physician and Minister, I have seen the power of modern medicine to bring about healing in the body and mind as well as the operation of the power of God to produce amazing medical results. However, many people are just not aware of the reality of divine healing. To some, it is a myth, belief or some "faith talk" in the heart. Medical miracles are real and we should take full advantage of it. As much as a love being a physician and treat patients in the hospital, I have come to see both its amazing successes and many limitations.

Industry/Entity Type

Christian

Font styles to use
Serif

Colors

Designer to choose colors to be used in the design.

Requirements
Should not have
• Too stylistic fonts

```html
<!DOCTYPE html>
<html lang="en">
<head>
<meta charset="utf-8">
<title>Forty Mornings to Claim and Hold Your Heavenly Restoration — Daniel Fesch</title>
<link rel="stylesheet" href="https://fonts.googleapis.com/css2?family=Cormorant+Garamond:ital,wght@0,500;0,600;0,700;1,500&display=swap">
<style>
  :root {
    --frame: #e9e9ea;
    --forest-deep: #161b1f;
    --forest-mid: #46545c;
    --mist: #a9b7bf;
    --light-glow: #f6f9fa;
    --beam: rgba(240, 246, 250, 0.22);
    --title: #dfe9f2;
    --title-shadow: rgba(20, 30, 40, 0.75);
    --tab-bg: #d9dcdf;
    --tab-text: #1e2226;
    --author: #eef0f1;
  }
  html, body {
    margin: 0;
    padding: 0;
    width: 822px;
    height: 1200px;
    overflow: hidden;
    background: var(--frame);
  }
  .cover {
    position: relative;
    width: 822px;
    height: 1200px;
    background: var(--frame);
    overflow: hidden;
  }
  .cover-art {
    position: absolute;
    inset: 10px;
    overflow: hidden;
    background:
      radial-gradient(ellipse 50% 40% at 10% 36%, var(--light-glow) 0%, rgba(244,247,248,0.6) 25%, rgba(244,247,248,0) 70%),
      radial-gradient(ellipse 30% 34% at 46% 80%, rgba(12,16,20,0.85) 0%, rgba(12,16,20,0.5) 50%, rgba(12,16,20,0) 100%),
      linear-gradient(90deg, rgba(20,26,30,0) 55%, rgba(20,26,30,0.55) 100%),
      linear-gradient(180deg, var(--forest-mid) 0%, var(--mist) 38%, var(--forest-mid) 68%, var(--forest-deep) 100%);
  }
  .light-beams {
    position: absolute;
    inset: 0;
    background:
      linear-gradient(118deg, transparent 30%, var(--beam) 33%, transparent 37%),
      linear-gradient(124deg, transparent 40%, var(--beam) 44%, transparent 49%),
      linear-gradient(130deg, transparent 50%, var(--beam) 53%, transparent 57%),
      linear-gradient(137deg, transparent 58%, var(--beam) 61%, transparent 65%);
    -webkit-mask-image: radial-gradient(ellipse 90% 70% at 8% 34%, #000 0%, rgba(0,0,0,0.6) 50%, transparent 85%);
    mask-image: radial-gradient(ellipse 90% 70% at 8% 34%, #000 0%, rgba(0,0,0,0.6) 50%, transparent 85%);
  }
  .title {
    position: absolute;
    inset: 0;
    margin: 0;
    font-family: "Cormorant Garamond", Georgia, serif;
    color: var(--title);
    text-shadow: 2px 3px 6px var(--title-shadow);
    line-height: 1;
    font-weight: 600;
  }
  .title-lead {
    position: absolute;
    left: 304px;
    top: 92px;
    font-style: italic;
    font-weight: 500;
    font-size: 27px;
    white-space: nowrap;
  }
  .title-line {
    position: absolute;
    white-space: nowrap;
    font-size: 96px;
    letter-spacing: 0.5px;
  }
  .title-line--first { left: 300px; top: 132px; }
  .title-line--second { left: 316px; top: 236px; }
  .series-tab {
    position: absolute;
    left: 566px;
    top: 562px;
    width: 246px;
    height: 40px;
    box-sizing: border-box;
    padding-left: 18px;
    background: var(--tab-bg);
    border-radius: 12px 0 0 12px;
    font-family: "Cormorant Garamond", Georgia, serif;
    font-weight: 700;
    font-size: 22px;
    line-height: 40px;
    color: var(--tab-text);
    white-space: nowrap;
  }
  .author {
    position: absolute;
    left: 424px;
    top: 1080px;
    margin: 0;
    font-family: "Cormorant Garamond", Georgia, serif;
    font-weight: 500;
    font-size: 24px;
    color: var(--author);
    white-space: nowrap;
  }
</style>
</head>
<body>
  <main class="cover">
    <div class="cover-art" role="img" aria-label="Misty forest with sunbeams of heavenly light falling on a silhouetted figure kneeling in prayer">
      <div class="light-beams"></div>
    </div>
    <h1 class="title">
      <span class="title-lead">Forty Mornings to Claim and Hold Your</span>
      <span class="title-line title-line--first">Heavenly</span>
      <span class="title-line title-line--second">Restoration</span>
    </h1>
    <div class="series-tab">Forty Morning Set</div>
    <p class="author">Daniel Fesch</p>
  </main>
</body>
</html>
```